Brightwell Homes needs a web design and brand identifier

Brightwell Homes is a pioneering approach by Calder councils and four greenhouse alliances to support low income households to install solar systems with no upfront costs.

Brightwell Homes will commence in May 2017.

Brightwell Homes is looking for a designer to create a website banner incorporating a brand identifier for Brightwell Homes. The brand identifier will be used in Brightwell Homes promotional materials, such as flyers and mail outs.

The website banner and brand identifier should engender trust and confidence in the target group (retirees).
Updates

Project Deadline Extended
Reason: Hi, Thank you for your work so far. We've been given advice to get a separate logo designed (instead of trying to include this as part of the banner design). Sorry for not realising this until now - we're new to all this. So, I have a couple of preliminary logo designs that are being considered by our project control group. I will forward a copy of the logo once we have it. The project control group is looking for a web design that is unique to Brightwell Homes and a design that draws on the key elements of the program (i.e. it helps people save money and take control). The site should be friendly but not too informal as the target group is seniors. Here's a link to another community energy organisation: www.kestrelgrid.com.au/ Apologies again for the delays. Cheers, Doug

Target Market(s)

Home owning, low income, retirees

Industry/Entity Type

Non Profit

Number of Pages Required

1 page

Font styles to use
Sans Serif

Requirements
Must have
• Use of Brightwell Home name
• Must promote Brightwell Homes as safe, reliable and trustworthy
Nice to have
• Blue - to engender sense of safety and confidence (open to suggestions, though)
• Solar panels / the sun
Should not have
• Anything that is hard to read
• anything that promotes riskyness

```html
<!DOCTYPE html>
<html lang="en">
<head>
<meta charset="utf-8">
<title>Brightwell Homes</title>
<link href="https://fonts.googleapis.com/css2?family=Montserrat:wght@700&family=PT+Serif:wght@400;700&family=Roboto:wght@400;500;700&display=swap" rel="stylesheet">
<style>
:root{
  --blue:#2f8fd8;
  --blue-dark:#1c6fb3;
  --orange:#f2a900;
  --ink:#222;
  --text:#444;
  --muted:#777;
  --grey-band:#ececec;
  --dark:#3b3b3b;
  --white:#fff;
}
*{box-sizing:border-box;margin:0;padding:0}
html,body{width:1200px;height:3965px;overflow:hidden;background:var(--white)}
body{position:relative;font-family:"PT Serif",Georgia,serif;color:var(--text)}
.sans{font-family:"Roboto",Arial,sans-serif}
section,header,footer{position:absolute;left:0;width:1200px}

/* header */
.site-header{top:0;height:74px;background:var(--white)}
.brand{position:absolute;left:86px;top:16px;display:flex;align-items:center;gap:10px}
.brand-mark{width:34px;height:34px;background:var(--blue);border-radius:50%}
.brand-name{font-family:"Roboto",Arial,sans-serif;font-weight:500;font-size:32px;color:var(--blue-dark);letter-spacing:-.5px}
.header-phone{position:absolute;right:140px;top:8px;font-family:"Roboto",Arial,sans-serif;font-size:14px;color:#333;display:flex;align-items:center;gap:6px}
.main-nav{position:absolute;left:500px;top:42px;display:flex;gap:27px;font-family:"PT Serif",serif;font-size:13px;color:#333;text-transform:uppercase}
.main-nav a{color:inherit;text-decoration:none}

/* hero */
.hero{top:74px;height:520px}
.hero-photo{position:absolute;inset:0;background:linear-gradient(180deg,#5c6a74 0%,#6f7d6a 45%,#5a6a3e 70%,#4c5a32 100%)}
.hero-copy{position:absolute;left:86px;top:118px;color:var(--white)}
.hero-copy h1{font-family:"Montserrat",Arial,sans-serif;font-size:66px;line-height:80px;font-weight:700}
.hero-copy p{font-family:"Roboto",Arial,sans-serif;font-size:16px;line-height:22px;width:640px;margin-top:10px}
.btn{display:inline-flex;align-items:center;height:36px;font-family:"Roboto",Arial,sans-serif;font-size:13px;color:var(--white);text-transform:uppercase;text-decoration:none}
.btn span{padding:0 18px}
.btn i{width:34px;height:36px;display:flex;align-items:center;justify-content:center;border-left:1px solid rgba(255,255,255,.5);font-style:normal}
.btn-orange{background:var(--orange)}
.btn-blue{background:var(--blue)}
.hero .btn{margin-top:20px}
.wave{position:absolute;left:0;width:1200px}

/* about */
.about{top:620px;height:440px}
.boxed-title{position:absolute;border:1px solid #ddd;box-shadow:0 2px 4px rgba(0,0,0,.12);font-family:"PT Serif",serif;font-weight:700;font-size:26px;color:var(--ink);text-transform:uppercase;padding:10px 16px;background:var(--white)}
.about .boxed-title{left:86px;top:28px}
.about-text{position:absolute;left:86px;top:115px;width:610px;font-size:14px;line-height:19px}
.about-text p{margin-bottom:14px}
.about .btn{position:absolute;left:86px;top:347px}
.collage .ph{position:absolute;border:4px solid var(--white);box-shadow:0 2px 6px rgba(0,0,0,.25)}
.ph-panels{left:761px;top:4px;width:232px;height:124px;background:linear-gradient(160deg,#8bb4d8,#2a5c93)}
.ph-person{left:712px;top:124px;width:242px;height:282px;background:linear-gradient(180deg,#8d9aa3,#c7b9a8 55%,#e7e1d8)}
.ph-turbines{left:956px;top:264px;width:188px;height:170px;background:linear-gradient(180deg,#6d9ed0,#a9c8e6 70%,#6f8a57)}

/* need */
.need{top:1084px;height:80px}
.need .boxed-title{left:86px;top:0;font-size:24px;padding:12px 10px}
.need-rule{position:absolute;left:300px;top:8px;width:3px;height:62px;background:var(--orange)}
.need p{position:absolute;left:316px;top:14px;width:860px;font-size:16px;line-height:23px}

/* how it works */
.how{top:1184px;height:516px}
.how-bg{position:absolute;inset:0;background:linear-gradient(180deg,#3b3326 0%,#5a4a2e 30%,#2e2a22 70%,#1f1d1a 100%)}
.how h2{position:absolute;top:40px;width:100%;text-align:center;color:var(--white);font-size:26px;font-weight:700;text-transform:uppercase}
.how .lead{position:absolute;top:82px;left:300px;width:600px;text-align:center;color:#eee;font-size:15px;line-height:20px}
.how-grid{position:absolute;left:145px;top:153px;width:908px;height:288px;display:grid;grid-template-columns:repeat(4,227px);grid-template-rows:repeat(2,144px)}
.how-card{background:var(--white);text-align:center;padding:20px 22px 0;font-family:"Roboto",Arial,sans-serif}
.how-card h3{font-size:14px;font-weight:500;color:#222;text-transform:uppercase;margin-bottom:6px}
.how-card p{font-size:12px;line-height:16px;color:#555}
.how-card a{display:inline-block;margin-top:8px;font-size:10px;color:var(--blue);text-transform:uppercase;text-decoration:none}
.how-photo{border:3px solid var(--white)}
.hp1{background:linear-gradient(150deg,#7fb2dd,#2a5d98)}
.hp2{background:linear-gradient(180deg,#b9c6cc,#8e8a6e 60%,#5f6e3c)}
.hp3{background:linear-gradient(150deg,#7aa6c9,#3c6a98 60%,#556b3a)}
.hp4{background:linear-gradient(160deg,#3a3834,#7d7057 50%,#a99e7b)}

/* eligible */
.eligible{top:1730px;height:390px}
.elig-photo{position:absolute;left:114px;top:14px;width:450px;height:358px;border:6px solid var(--white);box-shadow:0 2px 8px rgba(0,0,0,.25);background:linear-gradient(180deg,#9fc3e6 0%,#c9d8e6 40%,#4a6b9a 70%,#263f66)}
.eligible h2{position:absolute;left:628px;top:40px;font-size:27px;color:var(--ink);text-transform:uppercase}
.eligible h3{position:absolute;left:628px;top:84px;font-size:17px;color:var(--ink);text-transform:uppercase}
.eligible .intro{position:absolute;left:628px;top:116px;width:520px;font-size:14px;line-height:19px}
.check-list{position:absolute;left:628px;top:195px;list-style:none;width:560px}
.check-list li{display:flex;align-items:flex-start;gap:12px;font-size:16px;font-weight:700;color:#333;text-transform:uppercase;line-height:21px;padding:9px 0;border-bottom:1px solid #e4e4e4}
.check-list svg{flex:0 0 18px;margin-top:2px}

/* who */
.who{top:2154px;height:200px}
.who-bg{position:absolute;left:0;top:0;width:1200px;height:200px;background:linear-gradient(180deg,#2d2c2a,#4a4840 60%,#3a3934)}
.who h2{position:absolute;top:34px;width:100%;text-align:center;color:var(--white);font-size:21px;text-transform:uppercase}
.who p{position:absolute;top:66px;left:280px;width:640px;text-align:center;color:#eee;font-size:16px;line-height:21px}

/* streams */
.streams{top:2370px;height:530px}
.streams h2{position:absolute;top:20px;width:100%;text-align:center;font-size:27px;line-height:34px;color:var(--ink);text-transform:uppercase}
.streams svg{position:absolute;left:0;top:0}

/* clients */
.clients{top:2905px;height:280px;background:var(--grey-band)}
.clients h2{position:absolute;top:36px;width:100%;text-align:center;font-size:26px;font-weight:400;color:var(--ink);text-transform:uppercase}
.client-row{position:absolute;left:200px;top:92px;width:800px;display:flex;justify-content:space-between;align-items:center}
.client{display:flex;align-items:center;gap:6px;font-family:"PT Serif",serif;font-size:14px;font-weight:700;color:#1f4f86}
.client i{width:14px;height:14px;background:#1f4f86;border-radius:50%}

/* news */
.news{top:3150px;height:420px}
.news h2{position:absolute;top:40px;width:100%;text-align:center;font-size:26px;font-weight:400;color:var(--ink);text-transform:uppercase}
.news-card{position:absolute;top:88px;width:247px;height:318px;background:var(--white);box-shadow:0 1px 6px rgba(0,0,0,.18)}
.news-img{height:246px}
.ni1{background:linear-gradient(160deg,#4e8fd6,#9cc6ee 50%,#2c5a95)}
.ni2{background:linear-gradient(180deg,#8fb3d6,#3b5f8c 55%,#7e5b3a)}
.ni3{background:linear-gradient(170deg,#6fa2d2,#bcd6ee 60%,#8aa4b8)}
.news-date{position:absolute;right:0;top:0;width:64px;height:62px;background:var(--orange);color:var(--white);text-align:center;font-family:"Roboto",Arial,sans-serif;font-size:16px;line-height:20px;padding-top:10px}
.news-card h3{font-size:14px;font-weight:400;color:#333;line-height:18px;padding:18px 14px 0}
.news-arrow{position:absolute;top:212px;width:22px;height:22px}

/* footer */
.grass{position:absolute;left:0;top:3578px;width:1200px;height:64px;background:linear-gradient(180deg,rgba(214,190,140,0),#d8c79c 60%,#c9b27e)}
.site-footer{top:3630px;height:335px}
.footer-bg{position:absolute;left:0;top:0;width:1200px;height:335px}
.footer-brand{position:absolute;left:92px;top:92px;display:flex;align-items:center;gap:8px}
.footer-brand .brand-mark{width:28px;height:28px}
.footer-brand .brand-name{font-size:27px;color:var(--white)}
.footer-about{position:absolute;left:92px;top:150px;width:210px;color:#ddd;font-size:13px;line-height:17px}
.socials{position:absolute;left:92px;top:246px;display:flex;gap:14px}
.socials i{width:12px;height:12px;border-radius:50%;background:#ddd}
.footer-col h4{font-family:"PT Serif",serif;font-size:15px;color:var(--white);text-transform:uppercase;font-weight:400;margin-bottom:14px}
.footer-contact{position:absolute;left:370px;top:86px;width:290px;color:#ddd;font-size:12px;line-height:16px}
.footer-contact .row{display:flex;gap:8px;margin-bottom:12px}
.footer-contact .phone{font-family:"Roboto",Arial,sans-serif;font-size:18px;color:var(--white)}
.footer-links{position:absolute;left:695px;top:86px}
.footer-links ul{list-style:none}
.footer-links li{color:#ddd;font-size:12px;line-height:22.5px;padding-left:14px;position:relative}
.footer-links li::before{content:"";position:absolute;left:0;top:8px;width:6px;height:6px;border:1px solid #aaa;border-radius:50%}
.footer-gallery{position:absolute;left:914px;top:86px}
.gallery-img{width:222px;height:124px;background:linear-gradient(180deg,#8fb0cf,#c9d7e3 45%,#9a3e2e 75%,#6f6f6f)}
.gallery-dots{display:flex;gap:6px;justify-content:center;margin-top:8px}
.gallery-dots i{width:6px;height:6px;border-radius:50%;background:#888}
.gallery-dots i:first-child{background:var(--white)}
.copyright{position:absolute;left:92px;top:306px;color:#ccc;font-size:11px}
</style>
</head>
<body>

<header class="site-header">
  <div class="brand"><span class="brand-mark"></span><span class="brand-name">Brightwell Homes</span></div>
  <div class="header-phone">
    <svg width="10" height="14" viewBox="0 0 10 14"><rect x="1" y="1" width="8" height="12" rx="1.5" fill="none" stroke="#2f8fd8" stroke-width="1.5"/><circle cx="5" cy="11" r=".8" fill="#2f8fd8"/></svg>
    0400 555 271
  </div>
  <nav class="main-nav">
    <a href="#">Home</a><a href="#">About</a><a href="#">News</a><a href="#">Projects</a><a href="#">Advocacy</a><a href="#">Resources</a><a href="#">Contact</a>
  </nav>
</header>

<section class="hero">
  <div class="hero-photo" role="img" aria-label="Retired couple riding bicycles beside a tall solar panel under an evening sky"></div>
  <div class="hero-copy">
    <h1>Help pensioner<br>households</h1>
    <p>to save money and take control of their energy bills by installing an affordable, quality solar system and be part of an Australian first.</p>
    <a class="btn btn-orange" href="#"><span>Contact us</span><i>&#8250;</i></a>
  </div>
  <svg class="wave" style="top:470px" width="1200" height="50" viewBox="0 0 1200 50" preserveAspectRatio="none">
    <path d="M0 24 Q40 4 80 22 T160 20 T240 26 T320 18 T400 24 T480 20 T560 26 T640 18 T720 24 T800 20 T880 26 T960 18 T1040 24 T1120 20 T1200 22 V50 H0Z" fill="#fff"/>
  </svg>
</section>

<section class="about">
  <h2 class="boxed-title">About us</h2>
  <div class="about-text">
    <p>Brightwell Homes is a pioneering approach by councils to support pensioner households to save money and take control of their energy bills by installing affordable, quality solar systems with no upfront costs.</p>
    <p>Brightwell Homes, based on the City of Halloway's successful program, ensures that pension card households receive a solar system that pays for itself in electricity savings from day one.</p>
    <p>Brightwell Homes will be progressively rolled out across participating Calder municipalities through to June 2019. There are 20 participating councils and a limited number of opportunities for further councils to join.</p>
  </div>
  <a class="btn btn-blue" href="#"><span>Learn more</span><i>&#8250;</i></a>
  <div class="collage">
    <div class="ph ph-panels" role="img" aria-label="Rows of blue solar panels"></div>
    <div class="ph ph-person" role="img" aria-label="Smiling older man in a cap"></div>
    <div class="ph ph-turbines" role="img" aria-label="Wind turbines under a blue sky"></div>
  </div>
</section>

<section class="need">
  <h2 class="boxed-title">We needyou</h2>
  <span class="need-rule"></span>
  <p>Help pensioner households to save money and take control of their energy bills by installing an affordable, quality solar system and be part of an Australian first.</p>
</section>

<section class="how">
  <div class="how-bg" role="img" aria-label="Solar farm at dusk"></div>
  <h2>How it works</h2>
  <p class="lead">Nullam id luctus nibh. Mauris consectetur, est at placerat pretium, arcu turpis pulvinar eros, id malesuada odio lacus vitae nulla.</p>
  <div class="how-grid">
    <div class="how-photo hp1" role="img" aria-label="Installer fitting solar panels on a roof"></div>
    <div class="how-card"><h3>Installation</h3><p>Brightwell Homes organises for the solar system to be installed</p><a href="#">Read more &#8250;</a></div>
    <div class="how-photo hp2" role="img" aria-label="Older couple outside their home"></div>
    <div class="how-card"><h3>Payments</h3><p>Pensioners gradually pay for cost through their usual rates payments</p><a href="#">Read more &#8250;</a></div>
    <div class="how-card"><h3>Quality work</h3><p>Brightwell Homes checks that every person gets a solar system</p><a href="#">Read more &#8250;</a></div>
    <div class="how-photo hp3" role="img" aria-label="Solar panels on a house roof"></div>
    <div class="how-card"><h3>Help pensioner</h3><p>Brightwell Homes supports pensioners to understand</p><a href="#">Read more &#8250;</a></div>
    <div class="how-photo hp4" role="img" aria-label="Hands holding banknotes"></div>
  </div>
</section>

<section class="eligible">
  <div class="elig-photo" role="img" aria-label="Technician in a hard hat installing a solar panel"></div>
  <h2>Is my client eligible?</h2>
  <h3>Refer clients who are:</h3>
  <p class="intro">Nullam id luctus nibh. Mauris consectetur, est at placerat pretium, arcu turpis pulvinar eros, id malesuada odio lacus vitae nulla.</p>
  <ul class="check-list">
    <li><svg width="18" height="18" viewBox="0 0 18 18"><path d="M3 9.5l4 4 8-9" fill="none" stroke="#2f8fd8" stroke-width="2.6"/></svg>Homeowners</li>
    <li><svg width="18" height="18" viewBox="0 0 18 18"><path d="M3 9.5l4 4 8-9" fill="none" stroke="#2f8fd8" stroke-width="2.6"/></svg>Pension card holders</li>
    <li><svg width="18" height="18" viewBox="0 0 18 18"><path d="M3 9.5l4 4 8-9" fill="none" stroke="#2f8fd8" stroke-width="2.6"/></svg>Usually at home from 9am to 5pm</li>
    <li style="border-bottom:0"><svg width="18" height="18" viewBox="0 0 18 18"><path d="M3 9.5l4 4 8-9" fill="none" stroke="#2f8fd8" stroke-width="2.6"/></svg>Average to high electricity users<br>(contact Brightwell Homes if unsure)</li>
  </ul>
</section>

<section class="who">
  <div class="who-bg" role="img" aria-label="Solar panels against a darkened sky"></div>
  <svg class="wave" style="top:150px" width="1200" height="50" viewBox="0 0 1200 50" preserveAspectRatio="none">
    <path d="M0 22 Q50 2 100 20 T200 18 T300 26 T400 16 T500 24 T600 18 T700 26 T800 16 T900 24 T1000 18 T1100 24 T1200 18 V50 H0Z" fill="#fff"/>
  </svg>
  <h2>Who is Brightwell Homes?</h2>
  <p>Over 20 Calder councils have come together with support from the Calder State Government's Clean Power Jobs Fund to run the Brightwell Homes program.</p>
</section>

<section class="streams">
  <h2>Councils can choose to offer one<br>(or both) of the following streams:</h2>
  <svg width="1200" height="530" viewBox="0 0 1200 530">
    <defs>
      <marker id="arrowhead" markerWidth="8" markerHeight="8" refX="6" refY="4" orient="auto"><path d="M0 0 L7 4 L0 8" fill="none" stroke="#999" stroke-width="1.3"/></marker>
      <g id="node"><circle r="36" fill="#fff" stroke="#ccc" stroke-width="2"/><circle r="29" fill="#fff" stroke="#333" stroke-width="2"/></g>
      <g id="house"><path d="M-13 2 L0 -11 L13 2 M-9 -1 V12 H9 V-1" fill="none" stroke="#222" stroke-width="3"/><rect x="-3" y="4" width="6" height="8" fill="#222"/></g>
      <g id="bags"><circle cx="-10" cy="3" r="6" fill="#222"/><circle cx="0" cy="3" r="6" fill="#222"/><circle cx="10" cy="3" r="6" fill="#222"/><rect x="-12" y="-6" width="4" height="4" fill="#222"/><rect x="-2" y="-6" width="4" height="4" fill="#222"/><rect x="8" y="-6" width="4" height="4" fill="#222"/></g>
      <g id="building"><rect x="-10" y="-4" width="20" height="16" fill="#222"/><path d="M-13 -4 L0 -14 L13 -4Z" fill="#222"/><rect x="-6" y="0" width="3" height="8" fill="#fff"/><rect x="3" y="0" width="3" height="8" fill="#fff"/></g>
      <g id="card"><rect x="-11" y="-8" width="20" height="14" rx="2" transform="rotate(-25)" fill="#222"/><path d="M-12 10 L4 10 L10 2" fill="none" stroke="#222" stroke-width="3"/></g>
      <g id="coin"><circle r="10" fill="#222"/><rect x="-2" y="-16" width="4" height="8" fill="#222"/></g>
      <g id="bars"><rect x="-12" y="-10" width="24" height="20" fill="none" stroke="#222" stroke-width="2.5"/><rect x="-7" y="-5" width="14" height="4" fill="#222"/></g>
    </defs>

    <g fill="none" stroke="#aaa" stroke-width="2" marker-end="url(#arrowhead)">
      <path d="M380 150 Q450 170 480 222"/>
      <path d="M492 290 Q490 370 452 420"/>
      <path d="M390 460 Q330 480 290 455"/>
      <path d="M210 400 Q175 360 178 320"/>
      <path d="M215 225 Q250 165 300 150"/>
    </g>
    <circle cx="338" cy="307" r="92" fill="#f2a900"/>
    <text x="338" y="300" text-anchor="middle" font-family="Roboto, Arial, sans-serif" font-size="17" fill="#222">Council</text>
    <text x="338" y="322" text-anchor="middle" font-family="Roboto, Arial, sans-serif" font-size="17" fill="#222">Rates Stream</text>
    <g transform="translate(338 150)"><use href="#node"/><use href="#bags"/></g>
    <g transform="translate(484 250)"><use href="#node"/><use href="#card"/></g>
    <text x="484" y="308" text-anchor="middle" font-family="Roboto, Arial, sans-serif" font-size="15" fill="#222">Supplier</text>
    <g transform="translate(428 445)"><use href="#node"/><use href="#house"/></g>
    <g transform="translate(210 420)"><use href="#node"/><use href="#bars"/></g>
    <g transform="translate(180 240)"><use href="#node"/><use href="#building"/></g>
    <text x="165" y="305" text-anchor="middle" font-family="Roboto, Arial, sans-serif" font-size="15" fill="#222">Council</text>

    <path d="M500 430 Q600 400 690 290" fill="none" stroke="#bbb" stroke-width="2" stroke-dasharray="5 6" marker-end="url(#arrowhead)"/>

    <g fill="none" stroke="#aaa" stroke-width="2" marker-end="url(#arrowhead)">
      <path d="M935 150 Q1005 170 1035 215"/>
      <path d="M1048 290 Q1046 370 1010 420"/>
      <path d="M946 460 Q900 480 860 470"/>
      <path d="M760 430 Q730 400 722 350"/>
      <path d="M730 235 Q790 165 852 150"/>
    </g>
    <circle cx="893" cy="307" r="92" fill="#f2a900"/>
    <text x="893" y="290" text-anchor="middle" font-family="Roboto, Arial, sans-serif" font-size="17" fill="#222">Private Low</text>
    <text x="893" y="312" text-anchor="middle" font-family="Roboto, Arial, sans-serif" font-size="17" fill="#222">Interest Finance</text>
    <text x="893" y="334" text-anchor="middle" font-family="Roboto, Arial, sans-serif" font-size="17" fill="#222">Stream</text>
    <g transform="translate(893 150)"><use href="#node"/><use href="#bags"/></g>
    <g transform="translate(1043 250)"><use href="#node"/><use href="#card"/></g>
    <g transform="translate(985 445)"><use href="#node"/><use href="#house"/></g>
    <g transform="translate(800 460)"><use href="#node"/><use href="#bags"/></g>
    <g transform="translate(722 250)"><use href="#node"/><use href="#coin"/></g>
  </svg>
</section>

<section class="clients">
  <h2>Our clients</h2>
  <div class="client-row">
    <span class="client"><i></i>Halloway</span>
    <span class="client"><i></i>Westmere</span>
    <span class="client"><i></i>Corrindale</span>
    <span class="client"><i></i>Eastvale</span>
    <span class="client"><i></i>Ashby</span>
    <span class="client"><i></i>Kinross</span>
    <span class="client"><i></i>Tallow Ranges</span>
  </div>
  <svg class="wave" style="top:230px" width="1200" height="50" viewBox="0 0 1200 50" preserveAspectRatio="none">
    <path d="M0 26 Q60 6 120 24 T240 20 T360 28 T480 16 T600 24 T720 18 T840 28 T960 16 T1080 24 T1200 20 V50 H0Z" fill="#fff"/>
  </svg>
</section>

<section class="news">
  <h2>Latest news</h2>
  <svg class="news-arrow" style="left:146px" viewBox="0 0 22 22"><path d="M14 4 L6 11 L14 18Z" fill="#2f8fd8"/></svg>
  <svg class="news-arrow" style="left:1036px" viewBox="0 0 22 22"><path d="M8 4 L16 11 L8 18Z" fill="#2f8fd8"/></svg>
  <article class="news-card" style="left:193px">
    <div class="news-img ni1" role="img" aria-label="Solar panels against a bright blue sky"></div>
    <div class="news-date">02<br>Jun</div>
    <h3>The Solar Energy &amp;<br>Wind Energy</h3>
  </article>
  <article class="news-card" style="left:476px">
    <div class="news-img ni2" role="img" aria-label="House roof covered with solar panels"></div>
    <div class="news-date">08<br>Mar</div>
    <h3>Solar Panel Layout Project<br>-Phase I</h3>
  </article>
  <article class="news-card" style="left:756px">
    <div class="news-img ni3" role="img" aria-label="Wind turbines in a pale sky"></div>
    <div class="news-date">20<br>Jun</div>
    <h3>Intelligent use of<br>technology</h3>
  </article>
</section>

<div class="grass" role="img" aria-label="Grass border"></div>

<footer class="site-footer">
  <svg class="footer-bg" width="1200" height="335" viewBox="0 0 1200 335" preserveAspectRatio="none">
    <path d="M0 20 Q60 2 120 16 T240 14 T360 22 T480 10 T600 18 T720 12 T840 22 T960 10 T1080 18 T1200 12 V335 H0Z" fill="#3b3b3b"/>
  </svg>
  <div class="footer-brand"><span class="brand-mark"></span><span class="brand-name">Brightwell Homes</span></div>
  <p class="footer-about">Sed cursus tortor neque, sit amet dignissim purus pretium vel. Nullam at sodales sem.</p>
  <div class="socials"><i></i><i></i><i></i><i></i><i></i></div>

  <div class="footer-col footer-contact">
    <h4>Contact us</h4>
    <div class="row">
      <svg width="10" height="14" viewBox="0 0 10 14"><path d="M5 13 C1 8 0 6 0 5 A5 5 0 0 1 10 5 C10 6 9 8 5 13Z" fill="#ddd"/><circle cx="5" cy="5" r="1.8" fill="#3b3b3b"/></svg>
      <span>Ridgeline Alliance for Climate Action<br>Eastvale City Council<br>Larchmont Ave, Fernbrook</span>
    </div>
    <div class="row">
      <svg width="14" height="10" viewBox="0 0 14 10"><rect x=".5" y=".5" width="13" height="9" fill="none" stroke="#ddd"/><path d="M.5 .5 L7 6 L13.5 .5" fill="none" stroke="#ddd"/></svg>
      <span>doug.barlow@eastvale.gov.au</span>
    </div>
    <div class="row" style="align-items:center">
      <svg width="12" height="16" viewBox="0 0 12 16"><rect x="1" y="1" width="10" height="14" rx="2" fill="none" stroke="#ddd" stroke-width="1.5"/><circle cx="6" cy="12.5" r="1" fill="#ddd"/></svg>
      <span class="phone">0400 555 271</span>
    </div>
  </div>

  <div class="footer-col footer-links">
    <h4>Usefull links</h4>
    <ul>
      <li>Home</li><li>About</li><li>News</li><li>Projects</li><li>Advocacy</li><li>Resources</li><li>Contact</li>
    </ul>
  </div>

  <div class="footer-col footer-gallery">
    <h4>Gallery</h4>
    <div class="gallery-img" role="img" aria-label="Workers installing solar panels on a red roof"></div>
    <div class="gallery-dots"><i></i><i></i><i></i></div>
  </div>

  <p class="copyright sans">Copyright &copy; 2017 brightwell. all right reserved</p>
</footer>

</body>
</html>
```